J Lustra Gel Top Coat and Base Coat Promotion

We need an eye catching flyer sized 8.5"x11" to promote a new product to our customers. We are promoting our own brand of gel nail polish top coat and base coat to nail salon customers in the Northeast USA. Basic layout of flyer is attached, as well as our company logo and product pictures. Attached picture of small nail polish bottles is a sample picture only - it needs to be changed or altered to show 16 bottles (2 rows of 8 bottles).

Target Market(s)

retail nail salon owners in the Northeast USA

Industry/Entity Type

Nail

Font styles to use
Sans Serif
Other font styles liked:
• designers' choices

Requirements
Must have
• Basic layout with all the text, logo and pictures attached
• New or altered picture of 16 nail polish bottles: 2 rows of 8 each
Nice to have
• Different fonts and or colors, banners, borders, etc.

```html
<!DOCTYPE html>
<html lang="en">
<head>
<meta charset="utf-8">
<title>J Lustra Gel Top Coat &amp; Base Coat Flyer</title>
<link rel="stylesheet" href="https://fonts.googleapis.com/css2?family=Roboto+Condensed:wght@400;700&family=Roboto:wght@400;700;900&display=swap">
<style>
  :root {
    --page-bg: #ece9e4;
    --paper: #ffffff;
    --blue: #1f6fb8;
    --blue-light: #5ab0e3;
    --pink: #e64f63;
    --pink-soft: #f7c6cd;
    --ring: #e2364e;
    --ink: #2a2a2a;
    --dark: #262626;
    --clear-glass: #dfe3e6;
    --amber: #5a2e14;
  }
  * { box-sizing: border-box; margin: 0; padding: 0; }
  html, body { width: 1020px; height: 1200px; overflow: hidden; }
  body { background: var(--page-bg); font-family: "Roboto", Arial, sans-serif; position: relative; }

  .flyer {
    position: absolute; left: 60px; top: 18px; width: 900px; height: 1165px;
    background: var(--paper); overflow: hidden;
  }
  .swirl-decor {
    position: absolute; left: -120px; top: -60px; width: 1100px; height: 1250px;
    background:
      radial-gradient(ellipse 300px 380px at 150px 280px, rgba(240,120,140,.35), rgba(255,255,255,0) 70%),
      radial-gradient(ellipse 520px 640px at 980px 340px, rgba(247,198,205,.35), rgba(255,255,255,0) 60%),
      radial-gradient(ellipse 380px 420px at 260px 1050px, rgba(247,198,205,.45), rgba(255,255,255,0) 65%);
  }

  .headline {
    position: absolute; left: 47px; top: 52px;
    font-family: "Roboto Condensed", Arial, sans-serif; font-weight: 400;
    font-size: 58px; line-height: 62px; color: var(--ink);
  }
  .headline .blue { color: var(--blue); font-weight: 700; }
  .headline .pink { color: var(--pink); font-weight: 700; }

  .brand {
    position: absolute; left: 700px; top: 70px; width: 175px;
    display: flex; align-items: center; gap: 8px;
    font-family: "Roboto", Arial, sans-serif; font-weight: 700; font-size: 24px; color: var(--blue);
  }
  .brand-dot { width: 16px; height: 16px; border-radius: 50%; background: var(--blue); flex: none; }

  .feature-bar {
    position: absolute; left: 86px; top: 206px; width: 728px; height: 48px;
    background: linear-gradient(#f07a8a, var(--pink)); border-radius: 4px;
    box-shadow: 0 10px 12px -8px rgba(0,0,0,.35);
    display: flex; align-items: center; justify-content: space-evenly;
    font-family: "Roboto Condensed", Arial, sans-serif; font-size: 19px; color: #fff;
  }
  .feature-bar .sep { width: 1px; height: 26px; background: rgba(255,255,255,.8); }

  .bottle {
    position: absolute; width: 132px; height: 132px; border-radius: 50%;
    border: 3px solid var(--ring); background: var(--paper);
    box-shadow: 0 14px 10px -10px rgba(0,0,0,.3);
  }
  .bottle-photo {
    position: absolute; left: 8px; top: 8px; right: 8px; bottom: 8px; border-radius: 50%;
  }
  .bottle-photo.clear { background: radial-gradient(circle at 50% 55%, var(--clear-glass), #fff 75%); }
  .bottle-photo.amber { background: radial-gradient(circle at 50% 55%, var(--amber), #a0704c 55%, #fff 80%); }

  .refill-tag {
    position: absolute; left: 748px; top: 472px; width: 152px; height: 118px;
    color: #fff; text-align: center;
  }
  .refill-tag svg { position: absolute; inset: 0; }
  .refill-tag .tag-text { position: relative; padding: 6px 0 0 22px; font-weight: 900; line-height: 1; }
  .refill-tag .size { font-size: 34px; }
  .refill-tag .size small { font-size: 24px; }
  .refill-tag .label { font-size: 13px; font-weight: 700; margin-top: 2px; }
  .refill-tag .price { font-size: 28px; margin-top: 2px; text-decoration: underline; text-decoration-thickness: 2px; }
  .refill-tag .each { font-size: 13px; font-weight: 700; }

  .promise {
    position: absolute; left: 0; width: 900px; text-align: center; font-size: 27px;
  }
  .promise.love { top: 912px; color: var(--blue); left: 0; }
  .promise.refund { top: 950px; color: var(--pink); }

  .guarantee-badge { position: absolute; left: 60px; top: 986px; width: 126px; height: 142px; }
  .guarantee-badge .band {
    position: absolute; left: 0; top: 46px; width: 126px; height: 44px; background: #fff;
    text-align: center; font-family: "Roboto Condensed", Arial, sans-serif; font-weight: 700;
    font-size: 15px; line-height: 1.1; color: var(--dark); padding-top: 3px;
  }
  .guarantee-badge .band b { font-size: 17px; font-weight: 700; }

  .trial-seal {
    position: absolute; left: 201px; top: 1001px; width: 124px; height: 124px; border-radius: 50%;
    background: var(--pink); border: 3px solid #fff; box-shadow: 0 0 0 2px var(--pink);
    color: #fff; text-align: center; font-family: "Roboto Condensed", Arial, sans-serif;
    font-size: 22px; line-height: 1.05; padding-top: 26px;
  }
  .trial-seal b { font-weight: 700; }

  .price-pill {
    position: absolute; left: 401px; top: 1025px; width: 487px; height: 66px;
    background: var(--pink); border-radius: 33px 0 0 33px;
    color: #fff; font-weight: 700; font-size: 21px; line-height: 26px; padding: 8px 0 0 64px;
  }

  .footer-web {
    position: absolute; left: 0; top: 1142px; width: 501px; height: 23px; background: var(--blue-light);
    color: #fff; font-size: 15px; font-weight: 700; display: flex; align-items: center; padding-left: 178px; gap: 10px;
  }
  .footer-web .web-icon { width: 12px; height: 12px; border: 2px solid #fff; border-radius: 50%; }
  .footer-call {
    position: absolute; left: 487px; top: 1117px; width: 413px; height: 48px; background: var(--dark);
    clip-path: polygon(34px 0, 100% 0, 100% 100%, 0 100%);
    color: #fff; font-family: "Roboto Condensed", Arial, sans-serif; font-size: 25px;
    display: flex; align-items: center; padding-left: 90px;
  }
</style>
</head>
<body>
<main class="flyer">
  <div class="swirl-decor" role="img" aria-label="Soft pink floral swirl decoration"></div>

  <h1 class="headline">The <span class="blue">BEST</span> Gel <span class="blue">TOP COAT</span><br><span class="pink">BASE COAT</span> In The Market</h1>

  <div class="brand"><span class="brand-dot"></span>Coral Tide</div>

  <div class="feature-bar">
    <span>Super Shiny</span><span class="sep"></span><span>No Wipe</span><span class="sep"></span><span>No Chip</span><span class="sep"></span><span>Non Yellowing</span><span class="sep"></span><span>No Bad Smell</span>
  </div>

  <!-- row 1 -->
  <div class="bottle" style="left:123px;top:291px"><div class="bottle-photo clear" role="img" aria-label="Clear half-ounce gel bottle with black brush cap"></div></div>
  <div class="bottle" style="left:285px;top:291px"><div class="bottle-photo clear" role="img" aria-label="Clear half-ounce gel bottle with black brush cap"></div></div>
  <div class="bottle" style="left:447px;top:291px"><div class="bottle-photo clear" role="img" aria-label="Clear half-ounce gel bottle with black brush cap"></div></div>
  <div class="bottle" style="left:610px;top:291px"><div class="bottle-photo amber" role="img" aria-label="J Lustra Top Coat 8 oz amber refill bottle"></div></div>
  <!-- row 2 -->
  <div class="bottle" style="left:123px;top:454px"><div class="bottle-photo clear" role="img" aria-label="Clear half-ounce gel bottle with black brush cap"></div></div>
  <div class="bottle" style="left:285px;top:454px"><div class="bottle-photo clear" role="img" aria-label="Clear half-ounce gel bottle with black brush cap"></div></div>
  <div class="bottle" style="left:447px;top:454px"><div class="bottle-photo clear" role="img" aria-label="Clear half-ounce gel bottle with black brush cap"></div></div>
  <div class="bottle" style="left:610px;top:454px"><div class="bottle-photo amber" role="img" aria-label="J Lustra Top Coat 8 oz amber refill bottle"></div></div>
  <!-- row 3 -->
  <div class="bottle" style="left:123px;top:616px"><div class="bottle-photo clear" role="img" aria-label="Clear half-ounce gel bottle with black brush cap"></div></div>
  <div class="bottle" style="left:285px;top:616px"><div class="bottle-photo clear" role="img" aria-label="Clear half-ounce gel bottle with black brush cap"></div></div>
  <div class="bottle" style="left:447px;top:616px"><div class="bottle-photo clear" role="img" aria-label="Clear half-ounce gel bottle with black brush cap"></div></div>
  <div class="bottle" style="left:610px;top:616px"><div class="bottle-photo amber" role="img" aria-label="J Lustra Base Coat 8 oz amber refill bottle"></div></div>
  <!-- row 4 -->
  <div class="bottle" style="left:123px;top:778px"><div class="bottle-photo clear" role="img" aria-label="Clear half-ounce gel bottle with black brush cap"></div></div>
  <div class="bottle" style="left:285px;top:778px"><div class="bottle-photo clear" role="img" aria-label="Clear half-ounce gel bottle with black brush cap"></div></div>
  <div class="bottle" style="left:447px;top:778px"><div class="bottle-photo clear" role="img" aria-label="Clear half-ounce gel bottle with black brush cap"></div></div>
  <div class="bottle" style="left:610px;top:778px"><div class="bottle-photo amber" role="img" aria-label="J Lustra Base Coat 8 oz amber refill bottle"></div></div>

  <div class="refill-tag">
    <svg width="152" height="118" viewBox="0 0 152 118" aria-hidden="true">
      <polygon points="22,0 152,0 152,118 22,118 22,74 0,59 22,44" fill="var(--pink)"/>
    </svg>
    <div class="tag-text">
      <div class="size">8<small>oz.</small></div>
      <div class="label">Refill Bottle</div>
      <div class="price">$60/</div>
      <div class="each">Each</div>
    </div>
  </div>

  <p class="promise love">If you love it, You buy it</p>
  <p class="promise refund">If you don't love it, we pick up &amp; you pay $0</p>

  <div class="guarantee-badge">
    <svg width="126" height="142" viewBox="0 0 126 142" aria-hidden="true">
      <polygon points="63,0 126,71 63,142 0,71" fill="var(--blue)"/>
    </svg>
    <div class="band">SATISFACTION<br><b>GUARANTEED</b></div>
  </div>

  <div class="trial-seal">TEST FOR<br>2 WEEKS<br>FOR <b>FREE</b></div>

  <div class="price-pill">One Bottle $3.75 = .5 oz or<br>All Bottles $60 = 8 oz Each</div>

  <div class="footer-web"><span class="web-icon"></span>www.coraltidenail.com</div>
  <div class="footer-call">Call Us:555 010 2468</div>
</main>
</body>
</html>
```